Meridale Hair Studio Needs a new appointment business card

We need a new appointment card for our hair salon.

I Dont want bright out there colours.
I would like it to be neat, clean, easy to read. White, Black, with a hint of colour if needed.

We need
-Logo
-Phone number 47260385
-Mobile Number: 0417360528
Address: Shop 3/217 Tarrow Street, Kelby Court, Brenholt 4812

BACK SIDE OF CARD
- Appointment Time & Date (White background so we are able to write on it)
(If you are unable to make your appointment please contact us ASAP 47260385)

I also would like the chatterly and Snapfold logo(Find us on Chatterly)(find us on Snapfold)

Target Market(s)

appointment card simple to read. all information for their next appoint For all our clients male and female

Industry/Entity Type

Hairdresser

Contact Information for Business Card

-Logo
-Phone number 47260385

BACK SIDE OF CARD

Font styles to use
Serif
Sans Serif
Script

Requirements
Must have
• White Back ground on backside with appointment deatils so we are able to write information (like appointment time and date)
Nice to have
• Find us on Chatterly
and
snapfold - meridale_hairstudio
Should not have
• BRIGHT COLOURS

```html
<!DOCTYPE html>
<html lang="en">
<head>
<meta charset="utf-8">
<title>Meridale Hair Studio – Appointment Card</title>
<link href="https://fonts.googleapis.com/css2?family=Lato:wght@400;700;900&display=swap" rel="stylesheet">
<style>
  :root {
    --page: #e4e4e4;
    --card: #f6f6f4;
    --ink: #111111;
    --muted: #555555;
    --rule: #8a8a8a;
    --band-text: #ffffff;
  }
  * { box-sizing: border-box; margin: 0; padding: 0; }
  html, body {
    width: 1200px; height: 900px; overflow: hidden;
    background: var(--page);
    font-family: "Lato", sans-serif;
    color: var(--ink);
  }
  .sheet {
    width: 1200px; height: 900px;
    display: flex; align-items: center; justify-content: center; gap: 40px;
  }
  .card {
    position: relative;
    width: 540px; height: 310px;
    background: var(--card);
    box-shadow: 0 6px 18px rgba(0,0,0,0.12);
    overflow: hidden;
  }
  .brand {
    position: absolute;
    font-weight: 900; font-size: 24px; letter-spacing: 1px;
    text-transform: uppercase; white-space: nowrap;
  }

  /* appointment side */
  .appointment .brand { top: 40px; left: 0; right: 0; text-align: center; }
  .appointment .top-rule {
    position: absolute; top: 92px; left: 34px; right: 34px;
    border-top: 1px solid var(--rule);
  }
  .appointment .next {
    position: absolute; top: 112px; left: 34px;
    font-weight: 700; font-size: 17px; letter-spacing: 0.5px; white-space: nowrap;
  }
  .days {
    position: absolute; top: 114px; left: 232px; right: 34px;
    display: flex; justify-content: space-between; list-style: none;
    font-size: 13px; color: var(--muted); white-space: nowrap;
  }
  .days li { display: flex; align-items: center; gap: 5px; }
  .days li::before {
    content: ""; width: 10px; height: 10px; border-radius: 50%;
    border: 1.5px solid var(--ink);
  }
  .write-line {
    position: absolute; left: 216px; right: 34px;
    display: flex; align-items: flex-end; gap: 10px;
    font-weight: 700; font-size: 16px;
  }
  .write-line span.blank { flex: 1; border-bottom: 1px solid var(--rule); height: 18px; }
  .write-line.date { top: 158px; }
  .write-line.time { top: 198px; }
  .notice-band {
    position: absolute; left: 0; right: 0; bottom: 0; height: 50px;
    background: var(--ink); color: var(--band-text);
    display: flex; align-items: center; justify-content: center;
    font-size: 13.5px; letter-spacing: 0.2px; white-space: nowrap;
  }

  /* contact side */
  .contact .brand { top: 46px; right: 36px; }
  .find-us {
    position: absolute; top: 174px; right: 36px;
    display: flex; gap: 10px; align-items: baseline;
    font-size: 11.5px; white-space: nowrap;
  }
  .find-us .label { font-weight: 900; text-transform: uppercase; }
  .find-us .network { font-weight: 700; }
  .main-rule {
    position: absolute; left: 36px; right: 36px; top: 198px;
    border-top: 1.5px solid var(--ink);
  }
  .person { position: absolute; left: 36px; top: 138px; }
  .person .name { font-weight: 900; font-size: 24px; letter-spacing: 0.5px; text-transform: uppercase; white-space: nowrap; }
  .person .role { font-size: 14px; color: var(--muted); margin-top: 1px; }
  .phones { position: absolute; left: 36px; top: 214px; list-style: none; font-size: 14px; color: var(--muted); }
  .phones li { display: flex; align-items: center; gap: 10px; height: 22px; }
  .phones svg { width: 14px; height: 14px; }
  .address {
    position: absolute; right: 36px; top: 214px;
    text-align: right; font-size: 13.5px; line-height: 1.45; color: var(--muted);
    font-style: normal; white-space: nowrap;
  }
</style>
</head>
<body>
<main class="sheet">

  <section class="card appointment" aria-label="Appointment side">
    <div class="brand">Meridale Hair Studio</div>
    <div class="top-rule"></div>
    <div class="next">NEXT APPOINTMENT:</div>
    <ul class="days">
      <li>Mon</li><li>Tue</li><li>Wed</li><li>Thur</li><li>Fri</li>
    </ul>
    <div class="write-line date">Date: <span class="blank"></span></div>
    <div class="write-line time">Time: <span class="blank"></span></div>
    <div class="notice-band">If you are unable to make your appointment please contact us ASAP 47260385</div>
  </section>

  <section class="card contact" aria-label="Contact side">
    <div class="brand">Meridale Hair Studio</div>
    <div class="person">
      <div class="name">Daniel Reeve</div>
      <div class="role">Managing partner</div>
    </div>
    <div class="find-us">
      <span class="label">Find us on</span>
      <span class="network">Chatterly</span>
      <span class="network">Snapfold</span>
    </div>
    <div class="main-rule"></div>
    <ul class="phones">
      <li>
        <svg viewBox="0 0 16 16" aria-hidden="true"><path d="M2 6c0-2 3-3 6-3s6 1 6 3v1h-3V5.5H5V7H2z M4 8h8l1 6H3z" fill="#111"/><circle cx="8" cy="11" r="1.6" fill="#f6f6f4"/></svg>
        47260385
      </li>
      <li>
        <svg viewBox="0 0 16 16" aria-hidden="true"><rect x="4" y="1" width="8" height="14" rx="1.5" fill="none" stroke="#111" stroke-width="1.5"/><circle cx="8" cy="12.5" r="0.8" fill="#111"/></svg>
        0417360528
      </li>
    </ul>
    <address class="address">
      Shop 3/217 Tarrow Street,<br>Kelby Court, Brenholt 4812
    </address>
  </section>

</main>
</body>
</html>
```